Hollowmere Farm Promotional Leaflet

The team at Hollowmere Farm can help with every aspect of managing and enhancing your home from housekeeping and professional cleaning, laundry and ironing to providing chic and contemporary flower arrangements and even food for your pets!We take pride in providing high-end, consistent and reliable professional services bespoke to you. Whether you are a busy professional working long hours, a stay-at home parent or retired; having professional help in the home gives you time to spend on the things you enjoy.We are providing a very upmarket, highly professional service and need an A5 promotional leaflet to be designed. Please refer to www.hollowmerefarm-example.co.uk and see the section on 'Home Management'The leaflet should incorporate the Hollowmere Farm logo without the 'tipi', and any suitable photography images used on the home page of the website or the 'home management' section.

Target Market(s)

high-end, affluent owners of luxury homes

Industry/Entity Type

Farm

Contact Information for Business Card

The business card design needs to be suitable for use across all of Hollowmere Farm businesses, specifically:
Hollowmere Farm Home Management - otherwise known as Hollowmere Farm @ Home (this uses the typographical logo
Hollowmere Farm Weddings & Events - this uses the 'tipi' logo

Requirements
Must have
• Design in keeping with the look and feel of the logo and website design
• www.hollowmerefarm-example.co.uk

```html
<!DOCTYPE html>
<html lang="en">
<head>
<meta charset="utf-8">
<title>Hollowmere Farm Business Card</title>
<link href="https://fonts.googleapis.com/css2?family=Roboto:wght@400;500;700&display=swap" rel="stylesheet">
<style>
  :root {
    --canvas-bg: #efece8;
    --card-white: #ffffff;
    --brand-pink: #e0336d;
    --brand-pink-dark: #cf1f5c;
    --brand-gold: #e3b04b;
    --text-grey: #4a4a4a;
    --pattern-pink: #fbe6ee;
  }
  * { box-sizing: border-box; margin: 0; padding: 0; }
  html, body { width: 1200px; height: 911px; overflow: hidden; }
  body {
    background: var(--canvas-bg);
    font-family: "Roboto", Arial, sans-serif;
    position: relative;
  }
  .card {
    position: absolute;
    top: 305px;
    width: 520px;
    height: 300px;
    border-radius: 18px;
    background: var(--card-white);
    overflow: hidden;
    box-shadow: 0 6px 18px rgba(0,0,0,0.12);
  }
  .card--front { left: 50px; }
  .card--back { left: 630px; }

  .brand-band {
    position: absolute;
    right: 0; top: 0;
    width: 118px; height: 100%;
    background: linear-gradient(180deg, var(--brand-pink), var(--brand-pink-dark));
    display: flex; align-items: center; justify-content: center;
  }
  .brand-band__name {
    transform: rotate(90deg);
    white-space: nowrap;
    color: var(--card-white);
    font-size: 30px;
    font-weight: 500;
  }

  .contact {
    position: absolute;
    left: 34px; bottom: 30px;
    color: var(--text-grey);
    font-size: 14px;
    line-height: 1.4;
  }
  .contact__name {
    color: var(--brand-pink);
    font-weight: 700;
    font-size: 19px;
    letter-spacing: 0.3px;
  }
  .contact__role {
    color: var(--brand-gold);
    font-weight: 500;
    font-size: 14px;
    margin-bottom: 10px;
  }
  .contact__line { display: flex; align-items: center; gap: 7px; }
  .contact__icon { width: 12px; height: 12px; flex: none; }

  .pattern-field {
    position: absolute; inset: 0;
    background: var(--pattern-pink);
    opacity: 0.6;
  }
  .back-brand {
    position: absolute;
    left: 0; right: 0; top: 108px;
    text-align: center;
    color: var(--brand-pink);
    font-size: 44px;
    font-weight: 500;
  }
  .back-web {
    position: absolute;
    left: 0; right: 0; bottom: 30px;
    text-align: center;
    color: var(--text-grey);
    font-size: 13px;
    letter-spacing: 4px;
  }
</style>
</head>
<body>
  <section class="card card--front">
    <div class="brand-band"><span class="brand-band__name">Hollowmere Farm</span></div>
    <div class="contact">
      <p class="contact__name">THOMAS REED</p>
      <p class="contact__role">CEO/FOUNDER</p>
      <p>Hollowmere Farm</p>
      <p>Mill Lane, Brookhaven</p>
      <p>Wessex BH4 2RT, GB</p>
      <p class="contact__line">
        <svg class="contact__icon" viewBox="0 0 12 12" aria-hidden="true"><path d="M2.5 1 L4.5 1 L5 3.5 L3.8 4.4 Q4.8 6.8 7.6 8.2 L8.5 7 L11 7.5 L11 9.5 Q11 11 9.5 11 Q1 10 1 2.5 Q1 1 2.5 1 Z" fill="var(--brand-pink)"/></svg>
        +44 7000 555123
      </p>
      <p class="contact__line">
        <svg class="contact__icon" viewBox="0 0 12 12" aria-hidden="true"><circle cx="6" cy="6" r="6" fill="var(--brand-pink)"/><path d="M1 6 H11 M6 0.5 Q2.5 6 6 11.5 M6 0.5 Q9.5 6 6 11.5" stroke="#fff" stroke-width="0.9" fill="none"/></svg>
        www.hollowmerefarm-example.co.uk
      </p>
    </div>
  </section>

  <section class="card card--back">
    <div class="pattern-field" role="img" aria-label="Faint repeating brand-name pattern in pale pink"></div>
    <p class="back-brand">Hollowmere Farm</p>
    <p class="back-web">www.hollowmerefarm-example.co.uk</p>
  </section>
</body>
</html>
```